Criação de Papelaria para Arquitetura
A empresa queria:
" Escritório fundado por dois sócios ( Bordalo & Quintela ) com atuação desde a criação do projeto arquitetônico, compatibilização de projetos complementares e a construção - gerenciamento de obras. Maiores informações: www.bqarquitetos-exemplo.com.br "

```html
<!DOCTYPE html>
<html lang="pt-BR">
<head>
<meta charset="utf-8">
<title>Pasta institucional — Bordalo &amp; Quintela Arquitetos</title>
<link rel="stylesheet" href="https://fonts.googleapis.com/css2?family=Montserrat:wght@400;500&family=Cormorant+Garamond:wght@500&display=swap">
<style>
  :root {
    --bg: #e9e9ea;
    --paper: #ffffff;
    --fold: #e2e2e4;
    --ink: #4a4c50;
    --ink-soft: #6b6d72;
    --pocket: #595b5f;
    --photo-warm-a: #b08c62;
    --photo-warm-b: #5b4636;
    --photo-cool-a: #d9dde0;
    --photo-cool-b: #8f9599;
  }
  * { box-sizing: border-box; margin: 0; padding: 0; }
  html, body { width: 1200px; height: 1200px; overflow: hidden; }
  body { background: var(--bg); position: relative; font-family: "Montserrat", sans-serif; }

  .folder {
    position: absolute; left: 100px; top: 250px;
    width: 1000px; height: 700px;
    display: flex;
    box-shadow: 0 18px 40px rgba(0,0,0,0.12);
  }
  .panel { position: relative; width: 500px; height: 700px; background: var(--paper); overflow: hidden; }
  .panel--left { border-right: 1px solid var(--fold); }

  .photo {
    position: absolute; height: 120px;
    background: linear-gradient(135deg, var(--photo-warm-a), var(--photo-warm-b));
  }
  .photo--cool { background: linear-gradient(135deg, var(--photo-cool-a), var(--photo-cool-b)); }

  .brand {
    position: absolute; text-align: center;
    font-family: "Cormorant Garamond", serif; font-weight: 500;
    color: var(--ink); white-space: nowrap;
  }
  .brand--back { left: 0; right: 0; top: 560px; font-size: 34px; }
  .brand--inside { left: 40px; right: 40px; top: 44px; font-size: 26px; }

  .pocket-back {
    position: absolute; right: 0; bottom: 0; width: 150px; height: 14px;
    background: var(--pocket);
  }

  .about {
    position: absolute; left: 60px; right: 50px; top: 100px;
    color: var(--ink-soft); font-size: 10.5px; line-height: 1.5; text-align: justify;
  }
  .about p + p { margin-top: 10px; }

  .pocket { position: absolute; left: 0; bottom: 0; width: 500px; height: 290px; }
</style>
</head>
<body>
  <main class="folder">
    <section class="panel panel--left">
      <div class="photo" style="left:30px; top:80px; width:140px;" role="img" aria-label="Foto de fachada de loja em shopping com vitrines iluminadas"></div>
      <div class="photo" style="left:178px; top:80px; width:140px;" role="img" aria-label="Foto de loja com fachada em vidro e letreiro"></div>
      <div class="photo photo--cool" style="left:326px; top:80px; width:140px;" role="img" aria-label="Foto de interior de loja claro com balcões"></div>
      <div class="photo" style="left:30px; top:208px; width:214px;" role="img" aria-label="Foto de vitrine de loja de roupas em galeria"></div>
      <div class="photo photo--cool" style="left:252px; top:208px; width:214px;" role="img" aria-label="Foto de loja branca com expositores e iluminação"></div>

      <div class="brand brand--back">Bordalo &amp; Quintela</div>
      <div class="pocket-back"></div>
    </section>

    <section class="panel panel--right">
      <div class="brand brand--inside">Bordalo &amp; Quintela</div>

      <div class="about">
        <p>A Bordalo &amp; Quintela Arquitetos é uma empresa dedicada ao planejamento e execução de serviços de arquitetura e engenharia, com soluções voltadas para o mercado residencial e comercial.</p>
        <p>Com forte presença regional a partir de sua sede na cidade de São Paulo, a Bordalo &amp; Quintela oferece soluções completas para execução e gestão de projetos imobiliários.</p>
        <p>A Bordalo &amp; Quintela Arquitetos atua com uma equipe habilitada no processo de implantação de novas instalações, na identificação dos interesses do cliente e na defesa de seus interesses técnicos e econômicos.</p>
        <p>Uma empresa focada no cliente, provendo serviços integrados de implantação, da busca pelo espaço, estudo e viabilidade financeira, projetos de arquitetura e engenharia, gerenciamento de processos e logística de mudança.</p>
      </div>

      <svg class="pocket" viewBox="0 0 500 290" aria-hidden="true">
        <path d="M0 65 H70 C70 22 98 0 145 0 H500 V290 H0 Z" fill="var(--pocket)"/>
      </svg>
    </section>
  </main>
</body>
</html>
```